Design the web for "http://www.qlchatter.example"

QLChatter is an open source customer communication platform, think as BRAVOLINK.IO alternative.

QLChatter web site is an entry to let people know QLChatter and try QLChatter online QLChatter service.

1, To design the web site, suggest try QLChatter first.

2, At least replace the original pictures which QLChatter web site now use. (All got from cloudshelf site, shame and not reasonable)

3, Provide total web design, Picture and Code.

Thanks,
QLChatter owner
Haoran Wei
weihaoran@mailbox.example

Reason: So far no useful design, and only five designers submit their designs. And one man submit 48 designs, most of his design is same style. I request to extend the deadline, and invite more designers. Thanks, Haoran

Target Market(s)

Open Source.

Industry/Entity Type

Software

Coding

Coded - Design and coding required

Number of Pages Required

2 page

Font styles to use
Sans Serif

Requirements
Must have
• 1) Try QLChatter first
• 2) Replace all the pictures in the current site.
• 3) Match with the QLChattr features (Customer Communication / Open Source / Open API etc.)
• 4) Download page presents QLChatter support all kinds of platforms since QLChatter has all kinds of application for different OS.
• 5) Web style tuning (The current style copy from cloudshelf)
• 6) All pictures and web code.
Nice to have
• 1) Logo tuning for the new web style and logo file attached.
• 2) Extremely simple style is prefer.

```html
<!DOCTYPE html>
<html lang="en">
<head>
<meta charset="utf-8">
<title>QLChatter — Open Source Customer Communication Platform</title>
<link rel="stylesheet" href="https://fonts.googleapis.com/css2?family=Lato:wght@300;400;700;900&display=swap">
<style>
  :root {
    --ink-dark: #2b2b2b;
    --white: #ffffff;
    --blue: #1e88e5;
    --blue-button: #1b87f2;
    --grey-text: #8a8a8a;
    --hero-top: #74cddc;
    --hero-bottom: #62c2d3;
    --teal-light: #79d0de;
    --teal-mid: #56c4d5;
    --teal-deep: #4cb6c8;
    --teal-line: #5fc4d4;
    --teal-text: #48b9cc;
    --teal-faint: #86d9e5;
    --teal-sub: #3aa6b8;
    --footer: #4ea8b7;
    --footer-text: #7fd1de;
  }
  * { box-sizing: border-box; margin: 0; padding: 0; }
  html, body { width: 1200px; height: 2473px; overflow: hidden; }
  body { font-family: "Lato", Arial, sans-serif; background: var(--teal-light); position: relative; }

  /* header */
  .site-header { position: absolute; top: 0; left: 0; width: 1200px; height: 71px; background: var(--white); }
  .brand-block { position: absolute; left: 0; top: 0; width: 379px; height: 71px; background: var(--ink-dark); display: flex; align-items: center; padding-left: 100px; gap: 12px; }
  .brand-mark { width: 36px; height: 36px; background: var(--white); border-radius: 6px; }
  .brand-name { color: var(--white); font-size: 31px; font-weight: 700; letter-spacing: -0.5px; }
  .main-nav { position: absolute; top: 0; left: 0; }
  .main-nav a { position: absolute; top: 29px; color: var(--blue); font-size: 11px; font-weight: 700; text-decoration: none; white-space: nowrap; }

  /* hero */
  .hero { position: absolute; top: 71px; left: 0; width: 1200px; height: 679px; background: linear-gradient(180deg, var(--hero-top), var(--hero-bottom)); }
  .try-card { position: absolute; left: 193px; top: 191px; width: 807px; height: 425px; background: var(--white); box-shadow: 0 2px 10px rgba(0,0,0,.18); }
  .card-close { position: absolute; right: 18px; top: 16px; width: 20px; height: 20px; }
  .device-showcase { position: absolute; left: 186px; top: 53px; width: 453px; height: 234px; background: radial-gradient(ellipse at 55% 45%, #d9dde0 0%, #a7adb3 55%, #f2f3f4 100%); border-radius: 6px; }
  .card-title { position: absolute; left: 69px; top: 312px; font-size: 46px; font-weight: 300; color: var(--blue); line-height: 1; letter-spacing: .5px; }
  .card-tagline { position: absolute; left: 70px; top: 365px; font-size: 13px; color: var(--grey-text); line-height: 1.15; text-transform: uppercase; }
  .try-button { position: absolute; left: 542px; top: 327px; width: 129px; height: 36px; background: var(--blue-button); color: var(--white); font-size: 15px; font-weight: 700; display: flex; align-items: center; justify-content: center; gap: 9px; text-decoration: none; }

  /* welcome */
  .welcome { position: absolute; top: 750px; left: 0; width: 1200px; height: 483px; background: var(--teal-light); text-align: center; }
  .welcome-title { position: absolute; top: 68px; width: 100%; font-size: 46px; font-weight: 900; color: var(--teal-text); letter-spacing: 1px; }
  .welcome-lead { position: absolute; top: 124px; width: 100%; font-size: 25px; font-weight: 400; color: var(--teal-text); }
  .feature-ring { position: absolute; inset: 0; }
  .feature-label { position: absolute; width: 132px; text-align: center; font-size: 13px; line-height: 1.15; color: var(--teal-line); text-transform: uppercase; }
  .feature-label.active { color: var(--teal-faint); }
  .feature-label small { font-size: 11px; }

  /* integration */
  .integration { position: absolute; top: 1233px; left: 0; width: 1200px; height: 580px; background: var(--teal-mid); }
  .platform-drawing { position: absolute; left: 46px; top: 57px; width: 597px; height: 400px; background: radial-gradient(circle at 45% 50%, #63cadb 0%, #5ac6d7 45%, var(--teal-mid) 72%); }
  .integration-copy { position: absolute; left: 677px; top: 157px; width: 500px; }
  .integration-title { font-size: 35px; font-weight: 300; color: var(--teal-faint); line-height: 1.08; text-transform: uppercase; }
  .integration-sub { margin-top: 14px; font-size: 15px; font-weight: 700; color: var(--teal-sub); text-transform: uppercase; }
  .integration-list { list-style: disc; padding-left: 17px; color: var(--teal-faint); font-size: 11px; line-height: 18px; margin-top: 2px; }
  .integration-sub + .integration-list + .integration-sub { margin-top: 12px; }

  /* call to action */
  .start { position: absolute; top: 1813px; left: 0; width: 1200px; height: 376px; background: var(--teal-light); text-align: center; }
  .bubble-tail { position: absolute; left: 845px; top: 0; }
  .start-mark { position: absolute; left: 565px; top: 87px; width: 73px; height: 73px; border-radius: 6px; background: var(--teal-mid); }
  .start-title { position: absolute; top: 198px; width: 100%; font-size: 35px; font-weight: 300; color: var(--teal-text); }
  .start-button { position: absolute; left: 521px; top: 260px; width: 158px; height: 37px; background: var(--teal-mid); color: var(--teal-faint); font-size: 15px; font-weight: 700; display: flex; align-items: center; justify-content: center; text-decoration: none; }

  /* footer */
  .site-footer { position: absolute; top: 2189px; left: 0; width: 1200px; height: 284px; background: var(--footer); text-align: center; color: var(--footer-text); }
  .footer-brand { position: absolute; top: 95px; left: 0; width: 100%; display: flex; justify-content: center; align-items: center; gap: 12px; }
  .footer-mark { width: 46px; height: 46px; border-radius: 5px; background: var(--footer-text); }
  .footer-name { font-size: 36px; font-weight: 700; color: var(--footer-text); }
  .footer-links { position: absolute; top: 168px; width: 100%; font-size: 12px; font-weight: 700; }
  .footer-links a { color: var(--footer-text); text-decoration: none; }
  .footer-links span { margin: 0 12px; }
  .copyright { position: absolute; top: 198px; width: 100%; font-size: 16px; font-weight: 400; }
</style>
</head>
<body>

<header class="site-header">
  <div class="brand-block">
    <span class="brand-mark"></span>
    <span class="brand-name">qlchatter</span>
  </div>
  <nav class="main-nav">
    <a href="#" style="left:653px">HOME</a>
    <a href="#" style="left:739px">DOCUMENTATION</a>
    <a href="#" style="left:897px">DOWNLOAD</a>
    <a href="#" style="left:1022px">BLOG</a>
    <a href="#" style="left:1109px">FORUM</a>
  </nav>
</header>

<section class="hero" role="img" aria-label="Soft teal flat illustration of a work desk with keyboard, tablet, ruler, notebook and coffee cup">
  <div class="try-card">
    <svg class="card-close" viewBox="0 0 20 20" aria-hidden="true"><path d="M3 3 L17 17 M17 3 L3 17" stroke="#1e88e5" stroke-width="2.2"/></svg>
    <div class="device-showcase" role="img" aria-label="QLChatter apps shown on a desktop monitor, laptop, tablet and phone"></div>
    <h1 class="card-title">TRY QLCHATTER</h1>
    <p class="card-tagline">QLChatter is an open source customer<br>communication platform.</p>
    <a class="try-button" href="#">Try me
      <svg width="7" height="10" viewBox="0 0 7 10" aria-hidden="true"><path d="M0 0 L7 5 L0 10 Z" fill="#fff"/></svg>
    </a>
  </div>
</section>

<section class="welcome">
  <h2 class="welcome-title">WELCOME</h2>
  <p class="welcome-lead">QL CHATTER ia a plug and play communication platform.</p>
  <svg class="feature-ring" width="1200" height="483" viewBox="0 0 1200 483" aria-hidden="true">
    <g stroke="var(--teal-line)" stroke-width="3">
      <line x1="226" y1="265" x2="382" y2="265"/>
      <line x1="674" y1="265" x2="830" y2="265"/>
      <line x1="539" y1="440" x2="695" y2="440"/>
      <line x1="809" y1="440" x2="966" y2="440"/>
    </g>
    <g fill="none" stroke="var(--teal-line)" stroke-width="2.5">
      <circle cx="241" cy="354" r="64"/>
      <circle cx="527" cy="354" r="64"/>
      <circle cx="672" cy="354" r="64"/>
      <circle cx="814" cy="354" r="64"/>
      <circle cx="959" cy="354" r="64"/>
    </g>
    <path d="M384 288 A66 66 0 0 1 446 380 Q430 410 384 458 Q338 410 322 380 A66 66 0 0 1 384 288 Z" fill="var(--teal-mid)"/>
  </svg>
  <div class="feature-label" style="left:175px;top:339px">Open source<br>open API</div>
  <div class="feature-label active" style="left:318px;top:339px">Easy<br>integration</div>
  <div class="feature-label" style="left:461px;top:339px">Unified OAuth<br>framework</div>
  <div class="feature-label" style="left:606px;top:339px">Smart<br><small>communication</small></div>
  <div class="feature-label" style="left:748px;top:339px">Mobile<br>first</div>
  <div class="feature-label" style="left:893px;top:339px">Data<br>analysis</div>
  <svg style="position:absolute;left:372px;top:471px" width="24" height="12" viewBox="0 0 24 12" aria-hidden="true"><path d="M0 12 L12 0 L24 12 Z" fill="var(--teal-mid)"/></svg>
</section>

<section class="integration">
  <div class="platform-drawing" role="img" aria-label="Outline drawing of a desktop monitor, laptop, tablet and phone"></div>
  <div class="integration-copy">
    <h3 class="integration-title">Easy integration and<br>support all kinds of<br>platforms</h3>
    <p class="integration-sub">All kinds of platforms</p>
    <ul class="integration-list">
      <li>QLChatter backend runs on every major desktop and server system</li>
      <li>QLChatter service-end runs on desktop, laptop, tablet and phone</li>
      <li>QLChatter customer-end runs on web and mobile apps</li>
    </ul>
    <p class="integration-sub">Easy to use</p>
    <ul class="integration-list">
      <li>One line code integrate in customer-end</li>
      <li>One command to deploy QLChatter</li>
      <li>One directive integrate with manager user interface</li>
    </ul>
  </div>
</section>

<section class="start">
  <svg class="bubble-tail" width="168" height="99" viewBox="0 0 168 99" aria-hidden="true"><path d="M0 0 L168 0 L0 99 Z" fill="var(--teal-mid)"/></svg>
  <div class="start-mark"></div>
  <h2 class="start-title">GET STARTED WITH QLCHATTER FOR FREE</h2>
  <a class="start-button" href="#">Goto QLChatter</a>
</section>

<footer class="site-footer">
  <div class="footer-brand">
    <span class="footer-mark"></span>
    <span class="footer-name">qlchatter</span>
  </div>
  <p class="footer-links"><a href="#">TERMS &amp; CONDITIONS</a><span>|</span><a href="#">PRIVACY POLICY</a></p>
  <p class="copyright">©2010 - TODAY HARBOUR LANTERN SOFTWARE CO., LTD. ALL RIGHTS RESERVED</p>
</footer>

</body>
</html>
```